Designing a brochures for an educational counseling service provider

We would like a 4 sided design on a 11x8.5 paper, half folded. I have including a sample design we did to give you an idea of what we envision but we welcome creativity to make beautiful looking flyers. Text for the flier is included as well as our logo.
- The most important thing is capturing our audience/market. We will be handing these flies to schools, organizations and individual clients.

www.plorvaeducationalconsultants.example

Target Market(s)

We are targeting international students wanting to study in the U.S and Canada.

Industry/Entity Type

Education

Requirements
Must have
• - Clean and clear
• - Our logo should visible and well placed.
• - Could you the pictures of students, libraries and school buildings or you could use the pictures we already have.
Nice to have
• We would like this to match business cards.

```html
<!DOCTYPE html>
<html lang="en">
<head>
<meta charset="UTF-8">
<title>Plorva International Educational Consultants – Brochure Spread</title>
<link rel="stylesheet" href="https://fonts.googleapis.com/css2?family=Open+Sans:wght@700;800&family=Roboto:wght@400;500&family=Roboto+Condensed:wght@500;700&display=swap">
<style>
  :root {
    --navy: #14313f;
    --navy-deep: #0f2733;
    --orange: #f47b20;
    --orange-dark: #d9641a;
    --white: #ffffff;
    --ink: #111111;
    --grey-icon: #5a5a5a;
    --brand-blue: #1f4f8f;
    --photo-warm-1: #6b4a3a;
    --photo-warm-2: #c79a7c;
    --photo-cool-1: #3b3a40;
    --photo-cool-2: #b9b2ad;
  }
  html, body {
    margin: 0;
    padding: 0;
    width: 1200px;
    height: 927px;
    overflow: hidden;
    background: var(--white);
  }
  .spread {
    position: relative;
    width: 1200px;
    height: 927px;
    overflow: hidden;
    background: var(--white);
    font-family: "Roboto", Arial, sans-serif;
  }
  .layer {
    position: absolute;
    left: 0;
    top: 0;
    width: 1200px;
    height: 927px;
  }

  /* Back panel: contact */
  .contact {
    position: absolute;
    left: 15px;
    top: 544px;
    width: 360px;
    text-align: center;
    color: var(--ink);
  }
  .contact-title {
    margin: 0 0 6px;
    font-family: "Roboto Condensed", Arial, sans-serif;
    font-weight: 700;
    font-size: 29px;
    letter-spacing: 0.2px;
    color: var(--orange);
  }
  .contact-lines {
    margin: 0;
    font-size: 16px;
    line-height: 22px;
  }

  /* Front panel: brand */
  .brand {
    position: absolute;
    left: 650px;
    top: 60px;
    display: flex;
    align-items: center;
    gap: 18px;
  }
  .brand-mark {
    width: 84px;
    height: 84px;
    border-radius: 50%;
    background: var(--orange);
    flex: none;
  }
  .brand-name {
    font-family: "Roboto Condensed", Arial, sans-serif;
    font-weight: 700;
    color: var(--brand-blue);
    line-height: 1;
  }
  .brand-name .brand-word {
    display: block;
    font-size: 52px;
    letter-spacing: 1px;
  }
  .brand-name .brand-sub {
    display: block;
    font-size: 15px;
    letter-spacing: 0.4px;
    margin-top: 4px;
  }
  .brand-tagline {
    position: absolute;
    left: 756px;
    top: 177px;
    font-family: "Roboto", Arial, sans-serif;
    font-size: 10px;
    letter-spacing: 2.6px;
    color: var(--brand-blue);
  }

  .headline {
    position: absolute;
    left: 640px;
    top: 521px;
    width: 570px;
    margin: 0;
    text-align: center;
    font-family: "Open Sans", Arial, sans-serif;
    font-weight: 700;
    font-size: 19.5px;
    line-height: 21px;
    color: var(--white);
    text-transform: uppercase;
  }

  .services {
    position: absolute;
    left: 630px;
    top: 640px;
    margin: 0;
    padding: 0;
    list-style: none;
  }
  .service {
    display: flex;
    align-items: center;
    height: 51px;
  }
  .service-icon {
    width: 38px;
    height: 38px;
    flex: none;
  }
  .service-label {
    margin-left: 38px;
    font-family: "Roboto Condensed", Arial, sans-serif;
    font-weight: 700;
    font-size: 21px;
    color: var(--ink);
    letter-spacing: 0.2px;
  }
  .services-divider {
    position: absolute;
    left: 687px;
    top: 625px;
    width: 2px;
    height: 240px;
    background: #8a8a8a;
  }

  .footer-bar {
    position: absolute;
    left: 638px;
    top: 884px;
    font-family: "Roboto Condensed", Arial, sans-serif;
    font-weight: 700;
    font-size: 11px;
    color: var(--white);
    white-space: nowrap;
  }
</style>
</head>
<body>
<main class="spread">

  <!-- Structural shapes -->
  <svg class="layer" viewBox="0 0 1200 927" aria-hidden="true">
    <!-- top orange strip -->
    <polygon points="465,0 1200,0 1200,26 450,26" fill="var(--orange)"/>
    <!-- left navy bands -->
    <polygon points="330,0 422,0 0,655 0,470" fill="var(--navy)"/>
    <polygon points="432,0 452,0 170,448 150,448" fill="var(--navy)"/>
    <!-- center navy band -->
    <polygon points="735,205 890,205 300,927 245,927" fill="var(--navy)"/>
    <polygon points="538,458 545,458 275,927 262,927" fill="var(--navy)"/>
    <!-- top rule over photo -->
    <polygon points="862,221 1200,221 1200,229 856,229" fill="var(--navy)"/>
    <!-- bottom right orange bands -->
    <polygon points="880,605 1050,605 1200,800 1200,927 1120,927" fill="var(--orange)"/>
    <polygon points="1035,605 1050,605 1200,830 1200,850" fill="var(--orange-dark)"/>
    <!-- orange rule under photo -->
    <rect x="625" y="601" width="575" height="6" fill="var(--orange)"/>
    <!-- footer bar -->
    <polygon points="598,880 1048,880 1062,900 598,900" fill="var(--navy)"/>
  </svg>

  <!-- Photo areas -->
  <svg class="layer" viewBox="0 0 1200 927" role="img" aria-label="Photo of a smiling student carrying a shoulder bag">
    <defs>
      <linearGradient id="studentPortrait" x1="0" y1="0" x2="1" y2="1">
        <stop offset="0" stop-color="var(--photo-warm-1)"/>
        <stop offset="1" stop-color="var(--photo-warm-2)"/>
      </linearGradient>
    </defs>
    <polygon points="0,0 320,0 0,470" fill="url(#studentPortrait)"/>
  </svg>

  <svg class="layer" viewBox="0 0 1200 927" role="img" aria-label="Photo of a group of smiling international students together">
    <defs>
      <linearGradient id="studentGroup" x1="0" y1="0" x2="0" y2="1">
        <stop offset="0" stop-color="var(--photo-cool-2)"/>
        <stop offset="1" stop-color="var(--photo-cool-1)"/>
      </linearGradient>
    </defs>
    <polygon points="852,229 1200,229 1200,601 625,601 625,520 700,520" fill="url(#studentGroup)"/>
    <rect x="625" y="515" width="575" height="86" fill="#2b2b2b" opacity="0.55"/>
  </svg>

  <!-- Back panel -->
  <section class="contact">
    <h2 class="contact-title">CONTACT US</h2>
    <p class="contact-lines">
      Executive Director &amp; Independent<br>
      Educational Consultant<br>
      Plorva International Educational Consultants, LLC<br>
      1480 Meadow Ridge Rd<br>
      Suite 310, Linfield, TX 75010<br>
      Phone : 555-014-2870<br>
      Email : mara@plorvaeducationalconsultants.example
    </p>
  </section>

  <!-- Front panel -->
  <header class="brand">
    <span class="brand-mark" aria-hidden="true"></span>
    <span class="brand-name">
      <span class="brand-word">PLORVA</span>
      <span class="brand-sub">INTERNATIONAL EDUCATIONAL CONSULTANTS</span>
    </span>
  </header>
  <div class="brand-tagline">INTERNATIONAL STUDENTS SOLUTIONS</div>

  <h1 class="headline">A full-service international educational<br>consulting group serving students<br>and families across the globe.</h1>

  <div class="services-divider" aria-hidden="true"></div>
  <ul class="services">
    <li class="service">
      <svg class="service-icon" viewBox="0 0 38 38" fill="none" stroke="var(--grey-icon)" stroke-width="1.6" aria-hidden="true">
        <polygon points="4,13 19,4 34,13"/>
        <line x1="4" y1="15" x2="34" y2="15"/>
        <line x1="9" y1="17" x2="9" y2="29"/><line x1="15" y1="17" x2="15" y2="29"/>
        <line x1="23" y1="17" x2="23" y2="29"/><line x1="29" y1="17" x2="29" y2="29"/>
        <line x1="4" y1="31" x2="34" y2="31"/><line x1="2" y1="34" x2="36" y2="34"/>
      </svg>
      <span class="service-label">BOARDING SCHOOLS</span>
    </li>
    <li class="service">
      <svg class="service-icon" viewBox="0 0 38 38" fill="none" stroke="var(--grey-icon)" stroke-width="1.6" aria-hidden="true">
        <path d="M11 4 H25 L31 10 V34 H7 V8 Z"/>
        <path d="M25 4 V10 H31"/>
        <path d="M14 28 L26 16 L29 19 L17 31 L13 32 Z"/>
      </svg>
      <span class="service-label">COLLEGE ADMISSION</span>
    </li>
    <li class="service">
      <svg class="service-icon" viewBox="0 0 38 38" fill="none" stroke="var(--grey-icon)" stroke-width="1.6" aria-hidden="true">
        <circle cx="11" cy="11" r="5"/>
        <path d="M3 27 C3 20 19 20 19 27 V29 H3 Z"/>
        <circle cx="27" cy="18" r="5"/>
        <path d="M19 34 C19 27 35 27 35 34 V36 H19 Z"/>
        <line x1="2" y1="31" x2="17" y2="31"/>
      </svg>
      <span class="service-label">TRANSFER STUDENTS</span>
    </li>
    <li class="service">
      <svg class="service-icon" viewBox="0 0 38 38" fill="none" stroke="var(--grey-icon)" stroke-width="1.6" aria-hidden="true">
        <polygon points="2,13 19,5 36,13 19,21"/>
        <path d="M9 17 V27 C9 31 29 31 29 27 V17"/>
        <line x1="33" y1="14" x2="33" y2="26"/>
        <polygon points="31,30 33,25 35,30"/>
      </svg>
      <span class="service-label">GRADUATE STUDENTS</span>
    </li>
  </ul>

  <footer class="footer-bar">Linfield,Texas &nbsp; | &nbsp; +1-555-014-2870 &nbsp; | &nbsp; info@plorvaeducationalconsultants.example</footer>

</main>
</body>
</html>
```